Plumweave Inc. Website & Korvix Apps Landing Pages

We need a web site design for our company. We develop software and do various consultant projects for our clients. Our products focus on the mobile platform, mainly the Korvix (business, games, social, etc.). We want to communicate that our software is simple and good as candy. The web pages should be fun to look at not loosing seriousness and credibility. Web 2.0 style and 960 grid system a must. We are opened to any overall site colour scheme suggestions (look at the sites we like below).

Must haves:
- Our logo should be seen on the site and look great on it :-) (preview attached below)
- Main home page and app landing page.
- Section links/tabs on the home page (home,apps,support,blog,contact,about)
- No text in images
- Style sheet

Looks we like:
- http://x7k3lmq9pwrtzv.pixelmoorvault.net/412_Zelto_Site/final_large.jpg
- http://x7k3lmq9pwrtzv.pixelmoorvault.net/Premium_71_Illustrative_Korvix_Landing_Page/final.jpg
- http://grelmwick.com/
- http://dorniply.ca/
- http://quatzel.com/

Industry/Entity Type

Business

Requirements
Must have
• - Company logo should look great on pages.
• - Main home page and app landing page.
• - Section links/tabs on the home page (home,apps,support,blog,contact,about)
• - Web 2.0 style.
• - 960 grid system (12 col, 16 col).
• - Sliced ann optmized
• - Exported in all major formats (psd,ai,eps,png,jpeg,etc)
• - Style sheet
Should not have
• - Text in images

```html
<!DOCTYPE html>
<html lang="en">
<head>
<meta charset="utf-8">
<title>Plumweave — New App Title</title>
<link rel="stylesheet" href="https://fonts.googleapis.com/css2?family=Lexend:wght@600&family=Open+Sans:wght@400;600;700&display=swap">
<style>
  :root {
    --bar: #2e2d2c;
    --sky: #a3c6f8;
    --hero-end: #bfd7fb;
    --candy: #c8161d;
    --ink: #231a12;
    --text: #222;
    --muted: #444;
    --panel: #dcdcdc;
    --strip: #f4f0f0;
    --white: #fff;
  }
  * { box-sizing: border-box; margin: 0; padding: 0; }
  html, body { width: 1200px; height: 1200px; overflow: hidden; }
  body { position: relative; background: var(--white); font-family: "Open Sans", sans-serif; color: var(--text); }
  .abs { position: absolute; }

  .site-header { left: 0; top: 0; width: 1200px; height: 67px; background: var(--bar); }
  .brand { left: 130px; top: 14px; display: flex; align-items: center; gap: 10px; color: var(--white); font-weight: 700; font-size: 28px; }
  .brand-dot { width: 22px; height: 22px; border-radius: 50%; background: var(--candy); }
  .main-nav a { position: absolute; top: 22px; color: var(--white); font-weight: 700; font-size: 15px; text-decoration: none; }
  .main-nav .current::before { content: "{ "; color: var(--candy); }
  .main-nav .current::after { content: " }"; color: var(--candy); }

  .social-bar { left: 0; top: 68px; width: 1200px; height: 42px; background: var(--sky); border-top: 1px solid #dfe9f7; }
  .social-link { top: 13px; color: var(--white); font-size: 14px; }
  .social-dot { width: 34px; height: 34px; border-radius: 50%; background: #2c5aa0; border: 2px solid var(--white); }

  .hero { left: 0; top: 110px; width: 1200px; height: 384px; background: linear-gradient(var(--white) 10%, var(--hero-end)); }
  .app-title { left: 130px; top: 148px; font-family: "Lexend", sans-serif; font-weight: 600; font-size: 47px; color: var(--ink); letter-spacing: -1px; }
  .tab { top: 228px; width: 120px; height: 31px; background: linear-gradient(#e0262d, var(--candy)); border: 1px solid #9e1015; border-radius: 2px; color: var(--white); font-weight: 700; font-size: 14px; text-align: center; line-height: 29px; }
  .tab-active::after { content: ""; position: absolute; left: 52px; top: 30px; border: 7px solid transparent; border-top: 12px solid var(--candy); border-bottom: 0; }
  .intro { left: 131px; top: 286px; width: 450px; font-size: 15px; line-height: 24px; letter-spacing: .2px; }

  .more-projects { left: 931px; top: 135px; width: 126px; height: 84px; background: var(--white); border: 1px solid #ccc; border-radius: 2px; }
  .more-projects .pager { height: 56px; background: #1e1410; }
  .more-projects .label { text-align: center; font-weight: 700; font-size: 14px; line-height: 26px; color: var(--ink); }

  .features { left: 612px; top: 266px; width: 458px; height: 187px; background: var(--white); border: 1px solid #dde; }
  .side-label { position: absolute; left: 0; top: 0; bottom: 0; width: 43px; background: var(--strip); border-right: 1px solid #e4dede; }
  .side-label span { position: absolute; left: 50%; top: 50%; transform: translate(-50%, -50%) rotate(-90deg); font-weight: 700; font-size: 18px; letter-spacing: 1px; color: var(--ink); white-space: nowrap; }
  .feature { position: absolute; width: 190px; font-size: 13px; line-height: 24px; color: var(--muted); }
  .feature b { font-weight: 400; color: #000; }

  .screenshots { left: 130px; top: 494px; width: 940px; height: 187px; background: var(--panel); }
  .screenshots .side-label { border: 1px solid #ddd; }
  .shot { position: absolute; top: 20px; width: 261px; height: 145px; background: var(--white); border: 1px solid #ccc; border-radius: 2px; overflow: hidden; }
  .shot-art { position: absolute; top: 9px; width: 128px; height: 136px; border-radius: 16px 16px 0 0; background: linear-gradient(#111 0 32%, #d42a31 32%, #e9c8c2 100%); }

  .highlight { position: absolute; width: 290px; }
  .highlight h3 { font-weight: 400; font-size: 19px; color: var(--candy); line-height: 24px; }
  .highlight p { margin-left: 2px; font-size: 13.5px; line-height: 24px; color: var(--muted); letter-spacing: .2px; }

  .site-footer { left: 0; top: 1122px; width: 1200px; height: 78px; background: var(--bar); color: var(--white); }
  .footer-nav a { position: absolute; top: 15px; color: var(--white); font-size: 13px; text-decoration: none; }
  .copyright { position: absolute; left: 0; width: 1210px; top: 43px; text-align: center; font-size: 12px; }
</style>
</head>
<body>
  <header class="site-header abs">
    <div class="brand abs"><span class="brand-dot"></span>Plumweave</div>
    <nav class="main-nav">
      <a style="left:621px">home</a>
      <a class="current" style="left:676px">apps</a>
      <a style="left:750px">support</a>
      <a style="left:834px">blog</a>
      <a style="left:893px">contact</a>
      <a style="left:976px">about</a>
    </nav>
  </header>

  <div class="social-bar abs">
    <span class="social-link abs" style="left:620px">Follow us on Friendloop</span>
    <span class="social-dot abs" style="left:784px;top:4px"></span>
    <span class="social-link abs" style="left:858px">Follow us on Chirpwire</span>
    <span class="social-dot abs" style="left:1009px;top:4px;background:#2ea3d9"></span>
  </div>

  <section class="hero abs"></section>
  <h1 class="app-title abs">New App Title</h1>
  <div class="tab tab-active abs" style="left:143px">THE IDEA</div>
  <div class="tab abs" style="left:298px">THE RESULT</div>
  <p class="intro abs">Lorem ipsum dolor sit amet, consectetur adipiscing elit. Praesent erat eros, pharetra a consequat a, sagittis vel justo. Aliquam tempor felis vel orci tincidunt aliquet. Nunc sagittis, odio nec auctor tincidunt, mi neque euismod ipsum, at pretium arcu quam at nisl. Sed tellus eros, rhoncus vitae blandit quis, gravida ac felis. Aenean ante elit, ultrices non lacinia interdum, pretium in enim.</p>

  <div class="more-projects abs">
    <div class="pager">
      <svg width="124" height="56" viewBox="0 0 124 56"><path d="M50 9 L30 28 L50 47Z M76 9 L96 28 L76 47Z" fill="#f2eeee"/></svg>
    </div>
    <div class="label">more projects</div>
  </div>

  <section class="features abs">
    <div class="side-label"><span>FEATURES</span></div>
    <p class="feature" style="left:58px;top:40px"><b>Lorem ipsum</b> dolor sit amet, consectetur adipiscing elit.</p>
    <p class="feature" style="left:253px;top:40px">Lorem ipsum dolor sit amet, consectetur adipiscing elit.</p>
    <p class="feature" style="left:60px;top:112px">Lorem ipsum dolor sit amet, consectetur adipiscing elit.</p>
    <p class="feature" style="left:255px;top:112px">Lorem ipsum dolor sit amet, consectetur adipiscing elit.</p>
  </section>

  <section class="screenshots abs">
    <div class="side-label"><span>SCREENSHOTS</span></div>
    <div class="shot" style="left:73px"><div class="shot-art" style="left:70px" role="img" aria-label="Korvix phone showing the app's red and white candy screen"></div></div>
    <div class="shot" style="left:362px"><div class="shot-art" style="left:72px" role="img" aria-label="Korvix phone showing the app's red and white candy screen"></div></div>
    <div class="shot" style="left:651px"><div class="shot-art" style="left:61px" role="img" aria-label="Korvix phone showing the app's red and white candy screen"></div></div>
  </section>

  <article class="highlight" style="left:129px;top:724px"><h3>Highlight 1</h3><p>Lorem ipsum dolor sit amet, consectetur adipiscing elit. Quisque non ipsum enim. Nunc rhoncus pretium fringilla. Nulla id ...</p></article>
  <article class="highlight" style="left:453px;top:724px"><h3>Highlight 2</h3><p>Lorem ipsum dolor sit amet, consectetur adipiscing elit. Quisque non ipsum enim. Nunc rhoncus pretium fringilla. Nulla id ...</p></article>
  <article class="highlight" style="left:771px;top:724px"><h3>Highlight 3</h3><p>Lorem ipsum dolor sit amet, consectetur adipiscing elit. Quisque non ipsum enim. Nunc rhoncus pretium fringilla. Nulla id ...</p></article>
  <article class="highlight" style="left:128px;top:887px"><h3>Highlight 4</h3><p>Lorem ipsum dolor sit amet, consectetur adipiscing elit. Quisque non ipsum enim. Nunc rhoncus pretium fringilla. Nulla id ...</p></article>
  <article class="highlight" style="left:452px;top:887px"><h3>Highlight 5</h3><p>Lorem ipsum dolor sit amet, consectetur adipiscing elit. Quisque non ipsum enim. Nunc rhoncus pretium fringilla. Nulla id ...</p></article>
  <article class="highlight" style="left:770px;top:887px"><h3>Highlight 6</h3><p>Lorem ipsum dolor sit amet, consectetur adipiscing elit. Quisque non ipsum enim. Nunc rhoncus pretium fringilla. Nulla id ...</p></article>

  <footer class="site-footer abs">
    <nav class="footer-nav">
      <a style="left:261px">HOME</a>
      <a style="left:373px">APPS</a>
      <a style="left:477px">SUPPORT</a>
      <a style="left:596px">BLOG</a>
      <a style="left:720px">CONTACT</a>
      <a style="left:870px">ABOUT</a>
    </nav>
    <p class="copyright">Copyright 2010 Plumweave. All Rights Reserved</p>
  </footer>
</body>
</html>
```